Medical Clinic Group Looking for Website Design

We own and operate medical clinics and are looking looking to revamp our website. Our current website is www.marlowcarepartners.ca We need our website to be more functional, user friendly, and easier to maintain.

```html
<!DOCTYPE html>
<html lang="en">
<head>
<meta charset="utf-8">
<title>Marlow Care Partners</title>
<link rel="stylesheet" href="https://fonts.googleapis.com/css2?family=Poppins:wght@300;400;500;600&display=swap">
<style>
:root{
  --teal:#2ec4c9;
  --ink:#4a4a4a;
  --muted:#8a8a8a;
  --line:#e3e3e3;
  --panel:#f1f1f1;
  --footer:#6d6d6d;
  --footer-dark:#5e5e5e;
  --white:#ffffff;
}
*{box-sizing:border-box;margin:0;padding:0}
html,body{width:1200px;height:2748px;overflow:hidden}
body{font-family:"Poppins",sans-serif;color:var(--ink);background:var(--white)}
.container{width:960px;margin:0 auto;position:relative}
.btn{display:inline-block;font-size:15px;font-weight:500;padding:12px 26px;border-radius:4px;background:var(--teal);color:var(--white);text-decoration:none;white-space:nowrap}
.btn-dark{background:#6a6a6a}
.eyebrow{font-size:15px;font-weight:500;color:var(--teal);margin-bottom:6px}
.heading{font-size:40px;font-weight:500;line-height:1.2;color:var(--ink);margin-bottom:18px}
.copy{font-size:15px;line-height:1.75;color:var(--muted);margin-bottom:26px}

/* header */
.site-header{height:100px;display:flex;align-items:center}
.site-header .container{display:flex;align-items:center;justify-content:space-between}
.brand{display:flex;align-items:center;gap:12px;font-size:21px;font-weight:500;color:var(--teal);white-space:nowrap}
.brand-dot{width:28px;height:28px;border-radius:50%;background:var(--teal);flex:none}
.nav{display:flex;align-items:center;gap:36px;font-size:15px;color:var(--ink);white-space:nowrap}
.nav span.drop::after{content:" \25BE";color:var(--muted);font-size:12px}

/* hero */
.hero{height:540px;background:var(--panel);position:relative;overflow:hidden}
.hero .container{height:100%;display:flex;align-items:center}
.hero-text{width:420px;position:relative;z-index:2}
.hero-text .heading{font-size:44px}
.hero-photo{position:absolute;left:620px;top:135px;width:470px;height:270px;background:linear-gradient(120deg,#dfe9ea,#b9d4d8 55%,#e8eeee)}

/* quick links */
.quick-links{height:420px;display:flex;align-items:center}
.quick-grid{display:grid;grid-template-columns:repeat(3,1fr);width:840px;margin:0 auto}
.quick-item{height:160px;display:flex;flex-direction:column;align-items:center;justify-content:center;gap:16px;font-size:15px;color:var(--ink)}
.quick-item:nth-child(-n+3){border-bottom:1px solid var(--line)}
.quick-item:not(:nth-child(3n)){border-right:1px solid var(--line)}
.quick-item svg{width:46px;height:46px;stroke:var(--teal);fill:none;stroke-width:2;stroke-linecap:round;stroke-linejoin:round}

/* feature rows */
.feature{height:440px;position:relative;overflow:hidden}
.feature .container{height:100%;display:flex;align-items:center;gap:90px}
.feature-sports{background:linear-gradient(180deg,#ffffff,#eef3f4)}
.feature-booking{background:var(--panel)}
.feature-news{background:var(--white)}
.feature-text{width:440px}
.feature-text .heading{font-size:36px}
.diamond-wrap{position:relative;width:380px;height:380px;flex:none}
.diamond-photo{position:absolute;left:50%;top:50%;width:240px;height:240px;margin:-120px 0 0 -120px;border-radius:26px;transform:rotate(45deg)}
.photo-sports{background:linear-gradient(135deg,#d9e8ea,#9fc3c8)}
.photo-booking{background:linear-gradient(135deg,#c8dfe3,#6fa6b0)}
.photo-news{background:linear-gradient(135deg,#eef1f1,#c7d8da)}
.btn-row{display:flex;gap:14px}

/* footer */
.site-footer{height:368px;background:var(--footer);color:#e9e9e9}
.footer-main{height:308px;display:flex;align-items:flex-start;padding-top:70px}
.footer-main .container{display:flex;gap:56px}
.footer-brand{width:250px}
.footer-brand .brand{color:var(--white);font-size:19px}
.footer-col h4{font-size:16px;font-weight:500;color:var(--white);margin-bottom:14px}
.footer-col p{font-size:14px;line-height:1.9;color:#dcdcdc;white-space:nowrap}
.footer-bottom{height:60px;background:var(--footer-dark);display:flex;align-items:center;justify-content:center;font-size:13px;color:#cfcfcf}
</style>
</head>
<body>

<header class="site-header">
  <div class="container">
    <div class="brand"><span class="brand-dot"></span>Marlow Care Partners</div>
    <nav class="nav">
      <span>Locations</span>
      <span class="drop">Our Services</span>
      <span class="drop">For Providers</span>
      <span class="drop">About Us</span>
      <a class="btn" href="#">Book Online</a>
    </nav>
  </div>
</header>

<section class="hero">
  <div class="container">
    <div class="hero-text">
      <p class="eyebrow">Marlow Care Partners</p>
      <h1 class="heading">We simply providing care</h1>
      <p class="copy">Through our network of clinics we bring together skilled practitioners and trusted services so patients can find the care they need close to home, with less waiting and more support at every step.</p>
      <a class="btn btn-dark" href="#">More Info</a>
    </div>
  </div>
  <div class="hero-photo" role="img" aria-label="Doctor with stethoscope reviewing patient notes"></div>
</section>

<section class="quick-links">
  <div class="quick-grid">
    <div class="quick-item">
      <svg viewBox="0 0 48 48"><circle cx="24" cy="15" r="8"/><path d="M8 42c0-9 7-15 16-15s16 6 16 15"/></svg>
      Find a Provider
    </div>
    <div class="quick-item">
      <svg viewBox="0 0 48 48"><circle cx="17" cy="13" r="6"/><circle cx="33" cy="13" r="6"/><path d="M5 38c0-7 5-12 12-12s12 5 12 12M21 38c0-7 5-12 12-12s10 5 10 12"/></svg>
      Services
    </div>
    <div class="quick-item">
      <svg viewBox="0 0 48 48"><rect x="7" y="10" width="34" height="32" rx="3"/><path d="M7 19h34M16 6v8M32 6v8M18 30l4 4 8-8"/></svg>
      Book An Appointment
    </div>
    <div class="quick-item">
      <svg viewBox="0 0 48 48"><path d="M24 44s-14-13-14-24a14 14 0 0 1 28 0c0 11-14 24-14 24z"/><circle cx="24" cy="20" r="5"/></svg>
      Locations
    </div>
    <div class="quick-item">
      <svg viewBox="0 0 48 48"><path d="M12 5h18l8 8v30H12z"/><path d="M30 5v8h8M18 22h14M18 29h14M18 36h9"/></svg>
      Patient Resources
    </div>
    <div class="quick-item">
      <svg viewBox="0 0 48 48"><path d="M14 6l6 9-4 4c2 6 7 11 13 13l4-4 9 6-4 8C21 42 6 27 6 10z"/></svg>
      Contact Us
    </div>
  </div>
</section>

<section class="feature feature-sports">
  <div class="container">
    <div class="diamond-wrap">
      <div class="diamond-photo photo-sports" role="img" aria-label="Physiotherapist treating a patient's knee"></div>
    </div>
    <div class="feature-text">
      <p class="eyebrow">Your journey to health</p>
      <h2 class="heading">Sports medicine services now available at our Harbourview location</h2>
      <p class="copy">Our sports medicine team now offers assessment, treatment and recovery planning for active patients of all ages. Ask your family doctor for a referral or download the form below to get started.</p>
      <a class="btn btn-dark" href="#">Download Referral Form</a>
    </div>
  </div>
</section>

<section class="feature feature-booking">
  <div class="container">
    <div class="feature-text">
      <p class="eyebrow">Easy access to care when you need it</p>
      <h2 class="heading">Online appointment booking now available to all patients</h2>
      <p class="copy">Patients can now choose a time that suits them and book a visit in minutes from any device. Virtual sessions are also available for follow-ups and simple concerns.</p>
      <div class="btn-row">
        <a class="btn btn-dark" href="#">Book a Virtual Session</a>
        <a class="btn" href="#">Learn more</a>
      </div>
    </div>
    <div class="diamond-wrap">
      <div class="diamond-photo photo-booking" role="img" aria-label="Hands typing on a laptop keyboard to book an appointment"></div>
    </div>
  </div>
</section>

<section class="feature feature-news">
  <div class="container">
    <div class="diamond-wrap">
      <div class="diamond-photo photo-news" role="img" aria-label="Clinic staff member at the front desk"></div>
    </div>
    <div class="feature-text">
      <p class="eyebrow">We're innovating to serve you better</p>
      <h2 class="heading">Exciting things are happening!</h2>
      <p class="copy">We are adding new services, new practitioners and better tools across our clinics. Stay tuned for updates as we keep growing to meet the needs of our communities.</p>
      <a class="btn btn-dark" href="#">Read More</a>
    </div>
  </div>
</section>

<footer class="site-footer">
  <div class="footer-main">
    <div class="container">
      <div class="footer-brand">
        <div class="brand"><span class="brand-dot"></span>Marlow Care Partners</div>
      </div>
      <div class="footer-col">
        <h4>Locations</h4>
        <p>Westside Clinic<br>Harbourview Clinic<br>Northgate Clinic<br>Riverside Clinic</p>
      </div>
      <div class="footer-col">
        <h4>Contact us</h4>
        <p>(705) 555-0142<br>info@marlowcarepartners.ca<br>www.marlowcarepartners.ca<br>Open Mon to Fri, 8am to 6pm</p>
      </div>
      <div class="footer-col">
        <h4>Book online</h4>
        <p>Westside Medical Centre<br>Harbourview Sports Clinic<br>Northgate Family Practice</p>
      </div>
    </div>
  </div>
  <div class="footer-bottom">© 2024 Marlow Care Partners. All rights reserved.</div>
</footer>

</body>
</html>
```